we are an outdoor outlet in a country club that has a variety of outlets. The Club is called Brookhaven and is located in Palmvale, Egypt. This garden menu will include cuisines from the Mediterranean, Asia and Texmex. we need a menu that is colorful and would fit an A3 size, back and front are to be used. Attached is the old menu currently in use (Garden Menu 2012.pdf is just for reference) and the new menu text for you to use is under the name Garden Menu Fall 2013
thank you.

```html
<!DOCTYPE html>
<html lang="en">
<head>
<meta charset="utf-8">
<title>Brookhaven — Garden Menu</title>
<link rel="stylesheet" href="https://fonts.googleapis.com/css2?family=EB+Garamond:wght@400;500&family=Libre+Franklin:wght@800&display=swap">
<style>
  :root {
    --orange: #e2632b;
    --brown: #4b2a17;
    --brown-dark: #5a2f12;
    --lime: #b7c92b;
    --lime-soft: #eef3cf;
    --red-dot: #d9472a;
    --paper: #ffffff;
    --gutter: #d9d9d9;
  }
  * { margin: 0; padding: 0; box-sizing: border-box; }
  html, body { width: 1200px; height: 841px; overflow: hidden; background: var(--gutter); }
  body { position: relative; font-family: "EB Garamond", Georgia, serif; color: var(--brown); }

  .page { position: absolute; top: 0; width: 594px; height: 841px; background: var(--paper); overflow: hidden; }
  .page--front { left: 0; }
  .page--back { left: 606px; }

  .foliage { position: absolute; background: var(--lime); border-radius: 40% 40% 0 0 / 100% 100% 0 0; }
  .foliage--top { border-radius: 0 0 50% 50% / 0 0 100% 100%; }
  .plant-art { position: absolute; background: linear-gradient(180deg, rgba(238,243,207,0.15), rgba(226,234,176,0.55)); border-radius: 8px; }
  .dotted-rule { position: absolute; left: 0; right: 0; top: 820px; border-top: 2px dotted var(--red-dot); }

  .column { position: absolute; width: 262px; }
  .section { position: absolute; left: 0; width: 262px; }
  .section-title { font-weight: 400; font-size: 24px; line-height: 26px; color: var(--orange); margin-bottom: 12px; }
  .section-note { font-size: 7.5px; line-height: 9px; margin: -12px 0 10px; }

  .item { position: relative; margin-bottom: 8px; }
  .item-name { font-size: 13px; line-height: 15px; }
  .item-name small { font-size: 7.5px; }
  .item-desc { font-size: 7.5px; line-height: 9px; max-width: 205px; }
  .item-price { position: absolute; top: 0; left: 212px; font-size: 12px; line-height: 15px; }
  .option-line { font-size: 7.5px; line-height: 9px; margin-bottom: 8px; max-width: 260px; }

  .corner-title { position: absolute; font-family: "Libre Franklin", Arial, sans-serif; font-weight: 800; color: var(--brown-dark); text-align: center; line-height: 1.05; text-shadow: 0 0 2px #fff, 2px 2px 2px rgba(0,0,0,0.35); }
  .corner-rule { position: absolute; height: 10px; }

  .brand { position: absolute; text-align: center; color: var(--brown); font-weight: 400; }
  .brand-dot { display: block; margin: 0 auto 6px; width: 44px; height: 44px; border-radius: 50%; background: var(--lime); }
  .brand-name { font-size: 38px; line-height: 40px; }

  .tax-note { position: absolute; left: 46px; top: 801px; font-size: 9px; }
  .contact { position: absolute; left: 360px; top: 774px; width: 170px; text-align: center; font-size: 15px; line-height: 21px; }
  .contact-tel { color: var(--orange); }
</style>
</head>
<body>

<section class="page page--front">
  <div class="foliage foliage--top" style="left:250px;top:0;width:200px;height:22px" role="img" aria-label="Green leaf foliage along the top edge"></div>
  <div class="plant-art" style="left:20px;top:560px;width:330px;height:260px" role="img" aria-label="Faint palm tree line drawing"></div>

  <div class="brand" style="left:50px;top:78px;width:210px">
    <span class="brand-dot"></span>
    <div class="brand-name">Brookhaven</div>
  </div>

  <h1 class="corner-title" style="left:40px;top:187px;width:230px;font-size:30px">Mediterranean<br>Corner</h1>

  <div class="column" style="left:25px;top:0;height:841px">
    <div class="section" style="top:276px">
      <h2 class="section-title">Pizza &amp; Pasta:</h2>
      <div class="item" style="margin-bottom:5px"><div class="item-name">Pizza Margarita</div><div class="item-desc">(Choose your toppings) Create your own pasta</div><div class="item-price">L.E X.xx</div></div>
      <p class="option-line">Type: Spaghetti, Tagliatelle, Penne</p>
      <p class="option-line">Sauces: Napolitana, Bolognese, Alfredo</p>
      <p class="option-line">Toppings: Bell peppers, olives, tomato, onion Mushroom, chicken, tuna, pepperoni Smoked salmon, shrimps Lasagna</p>
    </div>

    <div class="section" style="top:404px">
      <h2 class="section-title">Sandwiches:</h2>
      <p class="section-note">(Served with French fries or a garden salad)</p>
      <div class="item"><div class="item-name">Beef or chicken shawerma</div><div class="item-price">L.E X.xx</div></div>
      <div class="item"><div class="item-name">Grilled kofta</div><div class="item-price">L.E X.xx</div></div>
      <div class="item"><div class="item-name">Greek lamb gyro</div><div class="item-desc">in pita bread with Tzatziki</div><div class="item-price">L.E X.xx</div></div>
      <div class="item"><div class="item-name">Club sandwich</div><div class="item-desc">with smoked beef, turkey, egg</div><div class="item-price">L.E X.xx</div></div>
    </div>

    <div class="section" style="top:557px">
      <h2 class="section-title">Main Courses:</h2>
      <div class="item"><div class="item-name">Veal parmeggiana</div><div class="item-desc">Breaded veal escalope topped with melted cheese and tomato sauce served with Spaghetti</div><div class="item-price">L.E X.xx</div></div>
      <div class="item"><div class="item-name">Chicken a la francaise</div><div class="item-desc">Pan fried chicken breast in a mushroom cream sauce with vegetables white rice</div><div class="item-price">L.E X.xx</div></div>
      <div class="item"><div class="item-name">Grilled salmon</div><div class="item-desc">Salmon steak charcoal grilled with avocado tomato relish and creamy mushroom risotto</div><div class="item-price">L.E X.xx</div></div>
      <div class="item"><div class="item-name">Moroccan chicken</div><div class="item-desc" style="max-width:190px">Chicken cubes simmered with spices and olives served with tomato rice</div><div class="item-price">L.E X.xx</div></div>
      <div class="item"><div class="item-name">Filet</div><div class="item-desc">Tender filet grilled to your liking served with mashed potato and creamed spinach</div><div class="item-price">L.E X.xx</div></div>
      <p class="option-line">Choice of sauces: Brown mushroom, Green Peppercorn, Gorgonzola</p>
    </div>
  </div>

  <div class="column" style="left:312px;top:0;height:841px">
    <div class="section" style="top:40px">
      <h2 class="section-title">Soup:</h2>
      <div class="item"><div class="item-name">Tomato basil</div><div class="item-desc">Simmered tomato soup finished with fresh basil and cream</div><div class="item-price">L.E X.xx</div></div>
      <div class="item"><div class="item-name">Chicken cream</div><div class="item-desc">Chicken broth with roasted chicken cubes, pine nuts, and cream</div><div class="item-price">L.E X.xx</div></div>
      <div class="item"><div class="item-name">Moroccan harira</div><div class="item-desc">Vegetable broth with fresh tomato, chickpeas, lentil, cilantro and diced lamb</div><div class="item-price">L.E X.xx</div></div>
    </div>

    <div class="section" style="top:180px">
      <h2 class="section-title">Appetizers:</h2>
      <div class="item"><div class="item-name">Salmon tartare</div><div class="item-desc">seasoned with lemon juice, garlic, and crushed black pepper</div><div class="item-price">L.E X.xx</div></div>
      <div class="item"><div class="item-name">Roasted eggplant rolls</div><div class="item-desc">with herbed ricotta cheese and pine nuts</div><div class="item-price">L.E X.xx</div></div>
      <div class="item"><div class="item-name">Falafel in mini pita</div><div class="item-desc">served with tehina and oriental salsa</div><div class="item-price">L.E X.xx</div></div>
      <div class="item"><div class="item-name">Mankousha</div><div class="item-desc">with thyme and olive oil</div><div class="item-price">L.E X.xx</div></div>
      <div class="item"><div class="item-name">Fried kobeba</div><div class="item-desc">with minced meat, spices, and pine nuts</div><div class="item-price">L.E X.xx</div></div>
      <div class="item"><div class="item-name">Fried calamari a la Romana</div><div class="item-desc">served with aioli</div><div class="item-price">L.E X.xx</div></div>
      <div class="item"><div class="item-name">Samboussek</div><div class="item-desc">with herbed white cheese and mint</div><div class="item-price">L.E X.xx</div></div>
      <div class="item"><div class="item-name">Oriental sausage</div><div class="item-desc">sautéed with garlic and onion</div><div class="item-price">L.E X.xx</div></div>
      <div class="item"><div class="item-name">Mini vine</div><div class="item-desc">leaves with a yoghurt dip</div><div class="item-price">L.E X.xx</div></div>
      <div class="item"><div class="item-name">Fatouch</div><div class="item-desc">with a pomegranate syrup dressing</div><div class="item-price">L.E X.xx</div></div>
      <div class="item"><div class="item-name">Hummus</div><div class="item-desc">seasoned with lemon juice, garlic, and olive oil</div><div class="item-price">L.E X.xx</div></div>
      <div class="item"><div class="item-name">White cheese</div><div class="item-desc">with diced tomato, thyme, and olive oil</div><div class="item-price">L.E X.xx</div></div>
      <div class="item"><div class="item-name">Tehina</div><div class="item-desc">seasoned with cumin, lemon juice, and garlic</div><div class="item-price">L.E X.xx</div></div>
    </div>

    <div class="section" style="top:637px">
      <h2 class="section-title">Salads:</h2>
      <div class="item"><div class="item-name">Caprese</div><div class="item-desc">Buffalo mozzarella and sliced tomato with a balsamic vinaigrette</div><div class="item-price">L.E X.xx</div></div>
      <div class="item"><div class="item-name">Rocket apple</div><div class="item-desc">Rocket leaves with gorgonzola, croutons, and strawberry vinaigrette</div><div class="item-price">L.E X.xx</div></div>
      <div class="item"><div class="item-name">French Riviera Nicoise</div><div class="item-desc">Lettuce, egg, tomato, tuna, olives, onion, celery, radish, bell pepper in a French vinaigrette</div><div class="item-price">L.E X.xx</div></div>
      <div class="item"><div class="item-name">Folle</div><div class="item-desc">Mixed greens with crab sticks, mushroom, corn, cherry tomato in a mango vinaigrette</div><div class="item-price">L.E X.xx</div></div>
    </div>
  </div>

  <div class="dotted-rule"></div>
  <div class="foliage" style="left:0;top:826px;width:594px;height:15px" role="img" aria-label="Green leaf foliage along the bottom edge"></div>
</section>

<section class="page page--back">
  <div class="foliage foliage--top" style="left:430px;top:0;width:160px;height:18px" role="img" aria-label="Green leaf foliage along the top edge"></div>
  <div class="plant-art" style="left:210px;top:170px;width:50px;height:330px" role="img" aria-label="Faint bamboo stalk line drawing"></div>
  <div class="plant-art" style="left:350px;top:150px;width:210px;height:350px" role="img" aria-label="Faint cactus line drawing"></div>

  <h1 class="corner-title" style="left:40px;top:35px;width:200px;font-size:29px">Asian Corner</h1>
  <svg class="corner-rule" style="left:18px;top:72px" width="236" height="10" viewBox="0 0 236 10" aria-hidden="true">
    <line x1="0" y1="5" x2="236" y2="5" stroke="#e2632b" stroke-width="2"/>
    <polygon points="118,0 124,5 118,10 112,5" fill="#e2632b"/>
  </svg>

  <h1 class="corner-title" style="left:40px;top:514px;width:200px;font-size:29px">Tex Mex</h1>
  <svg class="corner-rule" style="left:18px;top:549px" width="236" height="10" viewBox="0 0 236 10" aria-hidden="true">
    <line x1="0" y1="5" x2="236" y2="5" stroke="#e2632b" stroke-width="2"/>
    <polygon points="118,0 124,5 118,10 112,5" fill="#e2632b"/>
  </svg>

  <div class="column" style="left:18px;top:0;height:841px">
    <div class="section" style="top:94px">
      <h2 class="section-title">Salads &amp; Appetizers:</h2>
      <div class="item"><div class="item-name">Chicken wasabi salad</div><div class="item-desc">Diced chicken with a mayo wasabi dressing on top of shredded lettuce</div><div class="item-price">L.E X.xx</div></div>
      <div class="item"><div class="item-name">Chicken sesame noodle salad</div><div class="item-desc">Sesame crusted chicken with glass noodles tossed with sweet chili, soy sauce, and lemongrass</div><div class="item-price">L.E X.xx</div></div>
      <div class="item"><div class="item-name">Spring rolls</div><div class="item-desc">Vegetable spring rolls served with house made sweet and sour dip</div><div class="item-price">L.E X.xx</div></div>
      <div class="item"><div class="item-name">Indian samosa</div><div class="item-desc">Fried dough parcels filled with vegetables and spices</div><div class="item-price">L.E X.xx</div></div>
    </div>

    <div class="section" style="top:277px">
      <h2 class="section-title">Main Courses:</h2>
      <div class="item" style="margin-bottom:12px"><div class="item-name">Murgh chicken makhni</div><div class="item-desc">Chicken cubes in a rich creamy tomato sauce seasoned with garam masala<br>Choice of side: vegetable korma or curd</div><div class="item-price">L.E X.xx</div></div>
      <div class="item"><div class="item-name">Chicken tandoori</div><div class="item-desc">Grilled chicken cubes with tandoori spices served with basmati rice</div><div class="item-price">L.E X.xx</div></div>
      <div class="item" style="margin-bottom:12px"><div class="item-name">Thai coconut curry shrimp</div><div class="item-desc">Sautéed shrimp tossed with curry and coconut milk served with jasmine rice</div><div class="item-price">L.E X.xx</div></div>
      <div class="item"><div class="item-name">Mongolian beef</div><div class="item-desc">Soy marinated beef with oyster sauce and vegetables served with egg noodles</div><div class="item-price">L.E X.xx</div></div>
    </div>

    <div class="section" style="top:572px">
      <h2 class="section-title">Salads &amp; Appetizers:</h2>
      <div class="item"><div class="item-name">Caesar salad</div><div class="item-desc">Iceberg lettuce with Caesar dressing with grated Parmesan cheese and croutons</div><div class="item-price">L.E X.xx</div></div>
      <div class="item"><div class="item-name">Taco salad 42</div><div class="item-desc">Chicken breast, beans, sour cream, guacamole, tomato, corn, lettuce, olives, chives, vinaigrette</div><div class="item-price">L.E X.xx</div></div>
      <div class="item"><div class="item-name">Nachos</div><div class="item-desc">topped with chili, melted cheese, beans</div><div class="item-price">L.E X.xx</div></div>
      <div class="item"><div class="item-name">Chicken Quesadilla</div><div class="item-desc">served with guacamole, salsa, and sour cream</div><div class="item-price">L.E X.xx</div></div>
    </div>
  </div>

  <p class="tax-note">Prices are subjects to 12% service Charge and 10% Sales Tax</p>

  <div class="column" style="left:312px;top:0;height:841px">
    <div class="section" style="top:40px">
      <h2 class="section-title">Main Courses &amp;<br>Sandwiches:</h2>
      <div class="item"><div class="item-name">Cheese burger</div><div class="item-desc">House made lean beef burger topped with cheddar cheese</div><div class="item-price">L.E X.xx</div></div>
      <div class="item"><div class="item-name">Mushroom burger</div><div class="item-desc">Beef burger with sautéed mushroom, caramelized onion, and provolone cheese</div><div class="item-price">L.E X.xx</div></div>
      <div class="item"><div class="item-name">Crispy chicken wrap</div><div class="item-desc">Crisp fried chicken wrap with a ranch dressing</div><div class="item-price">L.E X.xx</div></div>
      <div class="item"><div class="item-name">Fajita <small>(Chicken, Beef, Combo)</small></div><div class="item-desc">pan seared meat or chicken with onion and bell pepper served with sour cream, guacamole, salsa</div><div class="item-price">L.E X.xx</div></div>
    </div>

    <div class="section" style="top:255px">
      <h2 class="section-title">Desserts:</h2>
      <div class="item"><div class="item-name">Mix berries cheesecake</div><div class="item-price">L.E X.xx</div></div>
      <div class="item"><div class="item-name">Crème brulee</div><div class="item-price">L.E X.xx</div></div>
      <div class="item"><div class="item-name">Chocolate caramel cake</div></div>
      <div class="item"><div class="item-name">Warm chocolate fondant</div><div class="item-price">L.E X.xx</div></div>
      <div class="item"><div class="item-name">Baked apple tart tatin</div><div class="item-price">L.E X.xx</div></div>
      <div class="item"><div class="item-name">Tiramisu</div><div class="item-price">L.E X.xx</div></div>
      <div class="item"><div class="item-name">Pumpkin pie flan</div><div class="item-price">L.E X.xx</div></div>
      <div class="item"><div class="item-name">Mixed berries granola yoghurt</div><div class="item-price">L.E X.xx</div></div>
      <div class="item"><div class="item-name">Vanilla ice cream</div><div class="item-desc">profiterole with dark and white chocolate sauce</div><div class="item-price">L.E X.xx</div></div>
      <div class="item"><div class="item-name">Caramelized banana</div><div class="item-desc">with Deep Fried Ice Cream</div><div class="item-price">L.E X.xx</div></div>
      <div class="item"><div class="item-name">Baklava</div><div class="item-desc">with Nuts and Sugar Syrup</div><div class="item-price">L.E X.xx</div></div>
      <div class="item"><div class="item-name">Shot glass sampler</div><div class="item-desc">Tiramisu, Chocolate Crisp Mousse, Pear with Sabayon</div><div class="item-price">L.E X.xx</div></div>
      <div class="item"><div class="item-name">Ice cream</div><div class="item-desc">by Scoop</div><div class="item-price">L.E X.xx</div></div>
    </div>
  </div>

  <div class="brand" style="left:340px;top:665px;width:210px">
    <span class="brand-dot"></span>
    <div class="brand-name">Brookhaven</div>
  </div>

  <div class="contact">
    <p>Contact us: Palmvale, Egypt</p>
    <p class="contact-tel">Tel: (02) 2735 4180</p>
  </div>

  <div class="dotted-rule"></div>
  <div class="foliage" style="left:0;top:826px;width:594px;height:15px" role="img" aria-label="Green leaf foliage along the bottom edge"></div>
</section>

</body>
</html>
```